Need a plumber

Would like a postcard sized flyer made up. Want the design to be kept very simple.
List of services we carry out in bullet point or similar.
Phone number and email included on the flyer.
Logo to feature prominantly.

List of services: Hot water issues
Burst Pipes
Gas Plumbing
Roof leaks
Drain blockages

Target Market(s)

Mums, dads and hosehgold owners

Industry/Entity Type

Plumbing

Colors
0054AA
0677BA
7BADD7
CADEEF
E8F1F8

Requirements
Must have
• Services we off and our logo, also must say "local plumber"

```html
<!DOCTYPE html>
<html lang="en">
<head>
<meta charset="utf-8">
<title>Clearwater Plumbing – Postcard Flyer</title>
<link rel="stylesheet" href="https://fonts.googleapis.com/css2?family=Oswald:wght@700&family=Montserrat:wght@800&family=Open+Sans:wght@700&family=Lato:wght@400&display=swap">
<style>
  :root{
    --page-bg:#8e8e8e;
    --brand-dark:#0054aa;
    --brand-mid:#0677ba;
    --brand-light:#7badd7;
    --brand-pale:#cadeef;
    --brand-mist:#e8f1f8;
    --ink:#454545;
    --black:#060606;
    --white:#ffffff;
  }
  *{margin:0;padding:0;box-sizing:border-box}
  html,body{width:1200px;height:1200px;overflow:hidden;background:var(--page-bg)}
  .flyer{position:absolute;left:166px;top:285px;width:870px;height:630px;background:var(--white);overflow:hidden}
  .flyer-art{position:absolute;inset:0}
  .headline{position:absolute;left:40px;top:110px;font-family:'Oswald',sans-serif;font-weight:700;color:var(--white);font-size:67px;line-height:59px;letter-spacing:-0.5px;text-transform:uppercase}
  .brand-badge{position:absolute;left:198px;top:27px;width:130px;height:130px;border-radius:50%;background:var(--black);border:3px solid var(--white);box-shadow:0 0 0 9px rgba(202,222,239,.75);display:flex;align-items:center;justify-content:center;text-align:center}
  .brand-name{font-family:'Oswald',sans-serif;font-weight:700;color:var(--white);font-size:15px;line-height:19px;letter-spacing:3px}
  .service-label{position:absolute;width:150px;text-align:center;font-family:'Montserrat',sans-serif;font-weight:800;font-size:17px;line-height:22px;color:var(--ink);text-transform:uppercase}
  .tagline{position:absolute;left:532px;top:530px;font-family:'Montserrat',sans-serif;font-weight:800;font-size:17px;line-height:22px;color:var(--brand-dark);text-transform:uppercase;letter-spacing:.5px}
  .call{position:absolute;left:122px;top:552px;color:var(--white)}
  .call-lead{font-family:'Montserrat',sans-serif;font-weight:800;font-size:17px;line-height:20px}
  .call-number{font-family:'Open Sans',sans-serif;font-weight:700;font-size:31px;line-height:38px;letter-spacing:.3px}
  .contact-list{position:absolute;left:532px;top:563px;list-style:none;font-family:'Lato',sans-serif;font-size:18px;line-height:23px;color:var(--ink)}
  .contact-list li{display:flex;align-items:center;gap:6px}
  .contact-list svg{width:14px;height:14px;flex:none}
</style>
</head>
<body>
<main class="flyer">
  <svg class="flyer-art" viewBox="0 0 870 630" width="870" height="630">
    <defs>
      <linearGradient id="blueField" x1="0" y1="0" x2="1" y2="1">
        <stop offset="0" stop-color="#1a78d0"/>
        <stop offset=".55" stop-color="#0a5fb8"/>
        <stop offset="1" stop-color="#1e8fd8"/>
      </linearGradient>
      <linearGradient id="photoTone" x1="0" y1="0" x2="1" y2="1">
        <stop offset="0" stop-color="#e9e6e0"/>
        <stop offset=".5" stop-color="#c9b79a"/>
        <stop offset="1" stop-color="#2d4f86"/>
      </linearGradient>
      <radialGradient id="iconFill" cx=".4" cy=".3" r=".8">
        <stop offset="0" stop-color="#2a7fd4"/>
        <stop offset="1" stop-color="#0a45a0"/>
      </radialGradient>
      <linearGradient id="swoosh" x1="0" y1="0" x2="1" y2="0">
        <stop offset="0" stop-color="var(--brand-dark)"/>
        <stop offset="1" stop-color="var(--brand-pale)"/>
      </linearGradient>
    </defs>

    <rect width="870" height="440" fill="url(#blueField)" role="img" aria-label="Blue-tinted view of plumbing pipes"/>
    <path d="M205 0 C260 60 300 150 355 200 L870 200 L870 0 Z" fill="#3fb6e0" opacity=".35"/>

    <path d="M270 0 L870 0 L870 283 C760 320 640 330 560 318 C480 305 430 260 395 228 C340 170 300 80 270 0 Z" fill="url(#photoTone)" role="img" aria-label="Photo of a plumber wearing a tool belt, holding a toolbox"/>
    <rect x="395" y="218" width="150" height="150" rx="6" fill="#1e2a33" opacity=".85" role="img" aria-label="Toolbox"/>

    <path d="M0 314 C120 380 250 418 393 418 C560 418 720 360 870 283 L870 630 L0 630 Z" fill="var(--white)"/>

    <g fill="#000" opacity=".05">
      <rect x="198" y="400" width="3" height="100"/>
      <rect x="364" y="420" width="3" height="100"/>
      <rect x="514" y="420" width="3" height="100"/>
      <rect x="671" y="400" width="3" height="100"/>
    </g>

    <g>
      <circle cx="127" cy="363" r="53" fill="var(--brand-pale)"/><circle cx="127" cy="363" r="45" fill="url(#iconFill)"/>
      <circle cx="282" cy="396" r="53" fill="var(--brand-pale)"/><circle cx="282" cy="396" r="45" fill="url(#iconFill)"/>
      <circle cx="439" cy="413" r="53" fill="var(--brand-pale)"/><circle cx="439" cy="413" r="45" fill="url(#iconFill)"/>
      <circle cx="596" cy="396" r="53" fill="var(--brand-pale)"/><circle cx="596" cy="396" r="45" fill="url(#iconFill)"/>
      <circle cx="744" cy="363" r="53" fill="var(--brand-pale)"/><circle cx="744" cy="363" r="45" fill="url(#iconFill)"/>
    </g>

    <g fill="none" stroke="var(--white)" stroke-width="2.2" stroke-linecap="round" stroke-linejoin="round">
      <path d="M101 360 q7-4 13 0 t13 0 t13 0 t13 0 M101 368 q7-4 13 0 t13 0 t13 0 t13 0 M101 376 q7-4 13 0 t13 0 t13 0 t13 0"/>
      <path d="M110 350 q-4-4 0-8 t0-8 M122 350 q-4-4 0-8 t0-8 M134 350 q-4-4 0-8 t0-8 M146 350 q-4-4 0-8 t0-8"/>
      <path d="M262 382 l14 3 l-3 12 l-14-3 z M302 382 l-14 3 l3 12 l14-3 z"/>
      <path d="M282 402 q-5 7 0 10 q5-3 0-10 z"/>
      <path d="M424 430 v-22 h30 v22 M418 430 h12 M448 430 h12 M439 408 v-8 M439 394 a4 4 0 1 0 0.01 0"/>
      <path d="M439 428 q-7-5 0-14 q7 9 0 14 z"/>
      <path d="M578 384 h30 v8 h-10 v18 h-6 v-18 h-14 z"/>
      <path d="M590 378 q-3 4 0 5 q3-1 0-5 z M600 378 q-3 4 0 5 q3-1 0-5 z M610 378 q-3 4 0 5 q3-1 0-5 z"/>
      <path d="M728 352 v14 a16 16 0 0 0 32 0 v-6 a8 8 0 0 0 -16 0 v10"/>
      <path d="M722 352 h12 M756 372 h12"/>
    </g>

    <path d="M190 495 C330 500 460 560 517 630 L450 630 Z" fill="url(#swoosh)"/>
    <path d="M0 547 C120 508 280 500 380 535 C420 550 450 590 471 630 L0 630 Z" fill="var(--black)"/>

    <g fill="none" stroke="var(--brand-mid)" stroke-width="2.6" stroke-linecap="round">
      <path d="M66 560 c-6 4 -8 10 -4 18 c5 10 14 20 24 25 c8 4 14 2 18 -3 l-8 -8 c-3 3 -6 4 -10 2 c-5-3 -9-8 -11-13 c-1-3 0-6 3-8 z"/>
      <path d="M88 560 a14 14 0 0 1 12 12 M90 552 a22 22 0 0 1 18 18"/>
    </g>
  </svg>

  <h1 class="headline">Need<br>Plumbing<br>Solution</h1>

  <div class="brand-badge"><span class="brand-name">CLEARWATER<br>PLUMBING</span></div>

  <p class="service-label" style="left:52px;top:420px">Hot Water<br>Issues</p>
  <p class="service-label" style="left:207px;top:455px">Burst Pipes</p>
  <p class="service-label" style="left:364px;top:472px">Gas<br>Plumbing</p>
  <p class="service-label" style="left:521px;top:455px">Roof Leaks</p>
  <p class="service-label" style="left:669px;top:420px">Drain<br>Blockages</p>

  <p class="tagline">Your Local Plumber</p>

  <div class="call">
    <p class="call-lead">CALL US TODAY!</p>
    <p class="call-number">+61 400 123 456</p>
  </div>

  <ul class="contact-list">
    <li><svg viewBox="0 0 14 14" fill="none" stroke="#0677ba" stroke-width="1.1"><rect x="1" y="3" width="12" height="8"/><path d="M1 3 l6 5 l6 -5 M1 11 l4.5-4 M13 11 l-4.5-4"/></svg>sam@clearwaterplumb.com</li>
    <li><svg viewBox="0 0 14 14" fill="none" stroke="#0677ba" stroke-width="1.1"><circle cx="7" cy="7" r="6"/><ellipse cx="7" cy="7" rx="2.6" ry="6"/><path d="M1 7 h12 M2 4 h10 M2 10 h10"/></svg>www.clearwaterplumb.com</li>
  </ul>
</main>
</body>
</html>
```